Movie Poster Design for the Independent documentary, BEYOND NINE

We are seeking a compelling and provocative poster design for our first independent film, Beyond Nine. This is the story of Mason Fellick, a relentlessly positive young man facing the last year of his life after 7 years of living with a rare and incurable cancer, osteosarcoma. We need to take this poster with us to Brightwater next week where we can share our story with potential distributors and industry executives. We have applied to other festivals this is the first of the season and we hope to be selected for others.

Mason Fellick is an inspiration to almost anyone he meets, he's charming, funny, human and a generous soul who does what ever he can to help the next guy or the next kid. Mason wants pediatric cancer to stop with him and he does all he can with his days to do that and still have fun and enjoy life. We can all learn a lot from Mason. Be sure to watch our trailer, like us on Chatterly and give us an amazing design! Many images of Mason are available for download on our website. www.beyondnine-film.org - we also had a Fundmoor campaign and there are images there too. We've liked MG_7107.jpg best for promotional pieces so far.

We have used an image of Mason for postcards that feels similar to the image of "The Woman by the Lantern" and some on our team like it's simplicity but that design can be enhanced too. As the co-director I am open, I really want to see some fresh creativity on this and so I invite you to submit your best work.

One small note, Mason loves orange and we do to so if you can weave that in somehow that would be awesome. If you prefer to work with high rez images email me and I will send you a link to our full rez images.

As for poster text here is what we have written and some links to look at

BEYOND NINE Poster

http://www.layoutharbor.net/2011/02/7-elements-of-a-great-movie-poster-design/

Beyond Nine – Poster credits – one sheet size 27" × 40" and scalable to 7 x 11

Title - Beyond Nine

Chose a tag line

"It’s all about perspective"

"What would you do with the last year of your life?"

"Never, never give up"

---------------------
MOVIE POSTER FONT for credits
Steel Tong font - http://www.quillbarn4.net/2009/12/the-movie-poster-font-you-were-looking-for/

Larger Font

A Delvane Production
A film by co-directors
Rosalind Techter
Noor Delvane

Produced by
Noor Delvane
Rosalind Techter

Smaller font
Co Produced by

Tarik Bel-Haddou
Samir Bel-Haddou
Pruett Family
Walter Brindle
Marcia Brindle
Al Brindle
Nadine Brindle
Lavanya Osei
Herbert J. Vossel
Colette Vossel
Tammy Corvell
Greg Corvell
Wendling Family
Morgan Dalquist
Nathaniel Dalquist

Written by
Mason T. Fellick
Rosalind Techter

Directors of Photography

Benjamin Thorvald
Daniel Pemberlin

Editor
Daniel Pemberlin
Ilse Varno

Production Associate
Rob Kettleby

Original Music
Paul Marcovich

Larger font
Coming Soon
Or
Watch this with someone you love

*we know we have alot of co producers names, one option might be to cut them or to find a creative way to deal with them all.

Thank you and happy creating!
The Beyond Nine Team

Target Market(s)

Young adults and families

Industry/Entity Type

Industry

Font styles to use
Serif
Other font styles liked:
• open to suggestions

Colors
3176b5
faa54c
f79020
cfdeed
919191
7f7f7f
000000
333333
d3d3d3

Requirements
Must have
• Positivity and feel real and authentic
Nice to have
• some enhancements
Should not have
• should not be sleek, high tech or all graphics

```html
<!DOCTYPE html>
<html lang="en">
<head>
<meta charset="utf-8">
<title>Beyond Nine — Poster</title>
<link rel="stylesheet" href="https://fonts.googleapis.com/css2?family=Tinos&family=Oswald:wght@300;400&family=Arimo&display=swap">
<style>
  :root {
    --ink: #000000;
    --orange: #f79020;
    --orange-soft: #faa54c;
    --paper: #ffffff;
    --skin-light: #e8c2a4;
    --skin-mid: #c99679;
    --skin-dark: #8a5a45;
  }
  * { margin: 0; padding: 0; box-sizing: border-box; }
  html, body { width: 813px; height: 1200px; overflow: hidden; background: var(--ink); }
  .poster {
    position: relative;
    width: 813px;
    height: 1200px;
    background: var(--ink);
    color: var(--paper);
    overflow: hidden;
  }
  .tagline {
    position: absolute;
    top: 8px; left: 0; width: 100%;
    text-align: center;
    font-family: "Arimo", Arial, sans-serif;
    font-weight: 400;
    font-size: 45px;
    line-height: 52px;
    color: var(--orange);
  }
  .portrait {
    position: absolute;
    left: 222px; top: 140px;
    width: 345px; height: 515px;
    border-radius: 48% 48% 10% 10% / 38% 38% 6% 6%;
    background: radial-gradient(ellipse at 50% 35%, var(--skin-light) 0%, var(--skin-mid) 60%, var(--skin-dark) 100%);
  }
  .subject-figure {
    position: absolute;
    left: 575px; top: 660px;
    width: 180px; height: 455px;
    border-radius: 40px 40px 10px 10px;
    background: linear-gradient(180deg, var(--skin-mid) 0%, #f2f2f2 14%, #e6e0d2 55%, #c99679 82%, var(--orange) 100%);
  }
  .title {
    position: absolute;
    z-index: 2;
    left: 0; top: 505px; width: 813px;
    text-align: center;
    font-family: "Tinos", "Times New Roman", serif;
    font-weight: 400;
    font-size: 132px;
    line-height: 170px;
    color: var(--orange);
    letter-spacing: -1px;
    white-space: nowrap;
  }
  .release {
    position: absolute;
    left: 30px; top: 712px;
    width: 230px; height: 43px;
    border: 1px solid var(--paper);
    text-align: center;
    font-family: "Tinos", "Times New Roman", serif;
    font-size: 28px;
    line-height: 41px;
  }
  .credits {
    position: absolute;
    left: 245px; top: 700px;
    width: 320px;
    text-align: center;
    font-family: "Oswald", "Arial Narrow", sans-serif;
    font-weight: 400;
    font-variant: small-caps;
  }
  .credits p { white-space: nowrap; }
  .company { font-size: 20px; line-height: 40px; }
  .company .name { color: var(--orange); font-size: 30px; text-transform: uppercase; }
  .role { font-size: 19px; margin-top: 8px; line-height: 30px; }
  .names { font-size: 17px; line-height: 30px; }
  .names span { margin: 0 10px; }
  .co-role { margin-top: 12px; }
  .co-names { font-size: 13px; line-height: 30px; }
  .co-names span { margin: 0 4px; }
  .fine-print {
    position: absolute;
    left: 0; top: 1128px; width: 813px;
    text-align: center;
    font-family: "Oswald", "Arial Narrow", sans-serif;
    font-weight: 300;
    font-variant: small-caps;
    font-size: 12px;
    line-height: 24px;
  }
  .fine-print small { font-size: 9px; margin-right: 4px; }
  .fine-print b { font-weight: 400; margin-right: 12px; }
</style>
</head>
<body>
<main class="poster">
  <h2 class="tagline">“What would you do<br>with the last year of your life?”</h2>

  <div class="portrait" role="img" aria-label="Close-up portrait of the film's subject, shaved head, bare shoulder, looking back over the shoulder"></div>

  <div class="subject-figure" role="img" aria-label="Full-length photo of the film's subject smiling and raising a peace sign, in a raglan tee, shorts and orange sneakers"></div>

  <h1 class="title">Beyond Nine</h1>

  <div class="release">Coming Soon</div>

  <section class="credits">
    <p class="company">A <span class="name">Delvane</span> Production</p>
    <p class="role">A film by co-directors</p>
    <p class="names"><span>Rosalind Techter</span><span>Noor Delvane</span></p>
    <p class="role">Produced by</p>
    <p class="names"><span>Noor Delvane</span><span>Rosalind Techter</span></p>
    <p class="role co-role">Co Produced by</p>
    <p class="co-names"><span>Tarik Bel-Haddou</span><span>Samir Bel-Haddou</span><span>Pruett Family</span><span>Walter Brindle</span></p>
    <p class="co-names"><span>Marcia Brindle</span><span>Al Brindle</span><span>Nadine Brindle</span><span>Lavanya Osei</span></p>
    <p class="co-names"><span>Herbert J. Vossel</span><span>Colette Vossel</span><span>Tammy Corvell</span><span>Greg Corvell</span></p>
    <p class="co-names"><span>Wendling Family</span><span>Morgan Dalquist</span><span>Nathaniel Dalquist</span></p>
  </section>

  <footer class="fine-print">
    <p><small>Written by</small><b>Mason T. Fellick &amp; Rosalind Techter</b><small>Directors of Photography</small><b>Benjamin Thorvald &amp; Daniel Pemberlin</b><small>Editors</small><b>Daniel Pemberlin &amp; Ilse Varno</b></p>
    <p><small>Production Associate</small><b>Rob Kettleby</b><small>Original Music</small><b>Paul Marcovich</b></p>
  </footer>
</main>
</body>
</html>
```